Broschüre KTR Festival
Zielgruppe
Wir sind ein Verband, der Ensembles der Amateurmusik (Blasorchester, Chöre, Akkordeonensembles ....) vertritt. Unsere Zielgruppe sind Menschen, die in ihrer Freizeit musizieren ebenso, wie Menschen die gerne Konzerte besuchen.
Die Broschüre ist ein Programmheft für ein eintägiges Festival mit mehreren Open-Air Bühnen.
Aufgabenstellung
Die Broschüre sollte DIN lang Format sein, damit sie gut in die Westentasche passt. Zentraler Bestandteil neben den Textseiten sind die Termintabellen, die die Auftritte auf den Bühnen abbilden.

```html
<!DOCTYPE html>
<html lang="de">
<head>
<meta charset="utf-8">
<title>KTR Festival – Broschüre</title>
<link href="https://fonts.googleapis.com/css2?family=Oswald:wght@300;700&family=Open+Sans:wght@400;700&family=Ubuntu:wght@500;700&display=swap" rel="stylesheet">
<style>
:root{
  --teal:#1b9a88;
  --teal-dark:#157f70;
  --coral:#e8604c;
  --yellow:#f2c12e;
  --plum:#4a2e4a;
  --blue:#1f6fb5;
  --green-head:#3aa37a;
  --ink:#555;
  --paper:#fff;
  --bg:#ececec;
}
*{box-sizing:border-box;margin:0;padding:0}
html,body{width:1200px;height:2954px;overflow:hidden}
body{background:var(--bg);font-family:"Open Sans",sans-serif;color:var(--ink);position:relative}
.section-label{position:absolute;left:24px;font:600 12px "Open Sans",sans-serif;letter-spacing:1.5px;color:#555}
.spread{position:absolute;left:24px;width:1152px;height:605px;overflow:hidden;background:var(--paper)}
.abs{position:absolute}
.pattern{position:absolute;background:linear-gradient(90deg,var(--coral) 0%,var(--yellow) 28%,var(--teal) 50%,var(--plum) 70%,var(--coral) 100%);opacity:.9}
.photo{position:absolute;background:linear-gradient(135deg,#8c8f86 0%,#c8c3b4 45%,#6e6a5e 100%)}
.brand{font-family:"Ubuntu",sans-serif;font-weight:700;color:var(--teal);line-height:1}
.brand-date{font-family:"Ubuntu",sans-serif;font-weight:500;color:var(--teal);line-height:1.15}
.title-cond{font-family:"Oswald",sans-serif;color:var(--teal);font-size:32px;line-height:1}
.title-cond .thin{font-weight:300}
.title-cond .bold{font-weight:700}
.body-copy{font-size:7px;line-height:14px;color:var(--ink)}
.justify{text-align:justify}
.partners{font-family:"Open Sans",sans-serif;font-weight:700;font-size:15px;color:#222;line-height:30px}
.partners span{display:flex;align-items:center;gap:6px}
.partners i{width:9px;height:9px;background:#222;border-radius:50%;display:inline-block}
.teal-field{position:absolute;background:var(--teal)}
.front-photo{position:absolute;background:linear-gradient(160deg,#3fae9e 0%,#1b9a88 45%,#147d6f 100%)}
.info-small{color:#fff;font-size:9px;line-height:12px}
.slogan{font-family:"Ubuntu",sans-serif;font-weight:700;color:#fff;font-size:26px;line-height:26px;text-transform:uppercase;text-align:center}
.artist h3{font-family:"Open Sans",sans-serif;font-weight:700;font-size:14px;color:var(--green-head)}
.artist h4{font-size:7.5px;font-weight:700;color:var(--coral);margin:2px 0 5px;text-transform:uppercase}
.artist h4 span{color:var(--teal)}
.artist p{font-size:7.6px;line-height:15px}
.artist.right{text-align:right}
.artist.right p{text-align:center}
.program-title{font-family:"Oswald",sans-serif;color:#fff;font-size:27px;line-height:1}
.program-title .thin{font-weight:300}
.program-title .bold{font-weight:700}
.slot{position:absolute;width:220px;color:#fff;border-bottom:1px dashed rgba(255,255,255,.55);padding-bottom:4px}
.slot.left{text-align:right}
.slot time{display:block;font-family:"Oswald",sans-serif;font-weight:300;font-size:18px;line-height:20px}
.slot strong{display:block;font-size:13px;line-height:16px}
.slot .conf{display:block;font-size:7.6px;font-weight:700;text-transform:uppercase;line-height:10px}
.slot .loc{display:block;font-size:7px;text-transform:uppercase;line-height:9px}
.tickets h2{font-family:"Ubuntu",sans-serif;font-weight:500;color:#fff;font-size:23px}
.tickets .phone{font-family:"Ubuntu",sans-serif;color:#fff;font-size:16px;margin-top:8px}
.tickets .mail{color:#fff;font-size:11px;font-weight:700}
</style>
</head>
<body>

<div class="section-label" style="top:76px">BROCHURE FRONTSIDE</div>

<section class="spread front" style="top:110px">
  <!-- festival text panel -->
  <div class="abs" style="left:79px;top:100px;width:90px">
    <div class="brand" style="font-size:22px">KTR<br>Festival</div>
    <div class="brand-date" style="font-size:14px;margin-top:8px">11.07.2020<br>Überlingen</div>
  </div>
  <h1 class="abs title-cond" style="left:146px;top:44px"><span class="thin">THE </span><span class="bold">FESTIVAL</span></h1>
  <p class="abs body-copy justify" style="left:170px;top:84px;width:112px">Lorem ipsum dolor sit amet, consectetur adipiscing elit, sed do eiusmod tempor incididunt ut labore et dolore magna aliqua. Ut enim ad minim veniam, quis nostrud exercitation ullamco laboris nisi ut aliquip ex ea commodo consequat.</p>
  <div class="abs body-copy justify" style="left:29px;top:210px;width:253px">
    <p>Duis aute irure dolor in reprehenderit in voluptate velit esse cillum dolore eu fugiat nulla pariatur. Excepteur sint occaecat cupidatat non proident, sunt in culpa qui officia deserunt mollit anim id est laborum.</p>
    <p style="margin-top:14px">Lorem ipsum dolor sit amet, consectetur adipiscing elit, sed do eiusmod tempor incididunt ut labore et dolore magna aliqua. Ut enim ad minim veniam, quis nostrud exercitation ullamco laboris nisi ut aliquip ex ea commodo consequat.</p>
    <p>Duis aute irure dolor in reprehenderit in voluptate velit esse cillum dolore eu fugiat nulla pariatur. Excepteur sint occaecat cupidatat non proident, sunt in culpa qui officia deserunt mollit anim id est laborum. Lorem ipsum dolor sit amet, consectetur adipiscing elit, sed do eiusmod tempor incididunt ut labore et dolore magna aliqua.</p>
  </div>

  <!-- partners -->
  <h2 class="abs title-cond" style="left:319px;top:42px;font-size:28px"><span class="thin">MAIN </span><span class="bold">PARTNERS</span></h2>
  <div class="abs partners" style="left:320px;top:82px">
    <span>Nordhafen</span>
    <span>Pastaria</span>
    <span>Trailwerk <i></i> Seelinie</span>
    <span>Voltaris</span>
  </div>

  <div class="pattern" role="img" aria-label="Geometrisches Muster aus Kreisen, Dreiecken und Streifen" style="left:0;top:415px;width:576px;height:190px;opacity:.75"></div>

  <!-- cover side -->
  <div class="front-photo" role="img" aria-label="Getöntes Foto eines Blasorchesters mit Notenständern" style="left:577px;top:0;width:575px;height:605px"></div>
  <svg class="abs" style="left:0;top:0" width="1152" height="605" viewBox="0 0 1152 605" aria-hidden="true">
    <path d="M853 0 H1152 V510 C990 505 853 340 853 0 Z" fill="#fff"/>
  </svg>
  <div class="pattern" role="img" aria-label="Geometrisches Muster in Koralle, Gelb und Türkis" style="left:980px;top:0;width:172px;height:150px"></div>
  <div class="pattern" role="img" aria-label="Geometrisches Muster" style="left:1070px;top:395px;width:82px;height:100px"></div>
  <div class="abs" style="left:973px;top:238px">
    <div class="brand" style="font-size:32px">KTR<br>Festival</div>
    <div class="brand-date" style="font-size:21px;margin-top:14px">11.07.2020<br>Überlingen</div>
  </div>
  <div class="abs slogan" style="left:920px;top:527px;width:170px">Natürlich<br>Musik!</div>

  <div class="abs" style="left:632px;top:514px">
    <div class="brand" style="color:#fff;font-size:13px">KTR<br>Festival</div>
    <div class="info-small" style="margin-top:4px">11.07.2020<br>Überlingen</div>
  </div>
  <div class="abs info-small" style="left:690px;top:520px">
    <div style="font-size:10px;font-weight:700">Info and Tickets</div>
    <div style="margin-top:10px;font-weight:700">+49 00 12 34 56 789</div>
    <div style="font-weight:700">tickets@ktrfestival.de</div>
    <div>www.ktrfestival.de</div>
  </div>
</section>

<div class="section-label" style="top:774px">BROCHURE BACKSIDE</div>

<section class="spread back" style="top:808px">
  <!-- left panel -->
  <div class="photo" role="img" aria-label="Foto eines Blasorchesters mit Notenständern im Freien" style="left:0;top:0;width:292px;height:186px"></div>
  <div class="abs artist" style="left:29px;top:197px;width:250px">
    <h3>Artist or Band Name</h3>
    <h4>Title of the theme - <span>Music start h 10.00</span></h4>
    <p>Lorem ipsum dolor sit amet, consectetur adipiscing elit, sed do eiusmod tempor incididunt ut labore et dolore magna aliqua. Ut enim ad minim veniam, quis nostrud exercitation ullamco laboris nisi ut aliquip ex ea commodo consequat.</p>
  </div>
  <div class="photo" role="img" aria-label="Foto eines Chors in weißer Kleidung auf einer Bühne" style="left:0;top:301px;width:292px;height:156px"></div>
  <div class="abs artist" style="left:29px;top:468px;width:250px">
    <h3>Artist or Band Name</h3>
    <h4>Title of the theme - <span>Music start h 10.00</span></h4>
    <p>Lorem ipsum dolor sit amet, consectetur adipiscing elit, sed do eiusmod tempor incididunt ut labore et dolore magna aliqua. Ut enim ad minim veniam, quis nostrud exercitation ullamco laboris nisi ut aliquip ex ea commodo consequat.</p>
  </div>

  <!-- program panel -->
  <div class="teal-field" style="left:292px;top:0;width:566px;height:566px"></div>
  <div class="pattern" role="img" aria-label="Geometrische Musterleiste" style="left:292px;top:0;width:566px;height:36px;opacity:.55"></div>
  <h2 class="abs program-title" style="left:369px;top:44px"><span class="thin">FESTIVAL </span><span class="bold">PROGRAM</span></h2>

  <div class="slot left" style="left:335px;top:76px"><time>09:30</time><strong>Event Title</strong><span class="conf">Festival press conference</span><span class="loc">Location goes here</span></div>
  <div class="slot left" style="left:335px;top:147px"><time>09:30</time><strong>Event Title</strong><span class="conf">Festival press conference</span><span class="loc">Location goes here</span></div>
  <div class="slot left" style="left:335px;top:218px"><time>09:30</time><strong>Event Title</strong><span class="conf">Festival press conference</span><span class="loc">Location goes here</span></div>
  <div class="slot left" style="left:335px;top:289px"><time>09:30</time><strong>Event Title</strong><span class="conf">Festival press conference</span><span class="loc">Location goes here</span></div>
  <div class="slot left" style="left:335px;top:360px"><time>09:30</time><strong>Event Title</strong><span class="conf">Festival press conference</span><span class="loc">Location goes here</span></div>
  <div class="slot left" style="left:335px;top:431px"><time>09:30</time><strong>Event Title</strong><span class="conf">Festival press conference</span><span class="loc">Location goes here</span></div>
  <div class="slot left" style="left:335px;top:502px;border-bottom:none"><time>09:30</time><strong>Event Title</strong><span class="conf">Festival press conference</span><span class="loc">Location goes here</span></div>

  <div class="slot" style="left:600px;top:47px"><time>09:30</time><strong>Event Title</strong><span class="conf">Festival press conference</span><span class="loc">Location goes here</span></div>
  <div class="slot" style="left:600px;top:118px"><time>09:30</time><strong>Event Title</strong><span class="conf">Festival press conference</span><span class="loc">Location goes here</span></div>
  <div class="slot" style="left:600px;top:189px"><time>09:30</time><strong>Event Title</strong><span class="conf">Festival press conference</span><span class="loc">Location goes here</span></div>
  <div class="slot" style="left:600px;top:260px"><time>09:30</time><strong>Event Title</strong><span class="conf">Festival press conference</span><span class="loc">Location goes here</span></div>
  <div class="slot" style="left:600px;top:331px"><time>09:30</time><strong>Event Title</strong><span class="conf">Festival press conference</span><span class="loc">Location goes here</span></div>
  <div class="slot" style="left:600px;top:402px"><time>09:30</time><strong>Event Title</strong><span class="conf">Festival press conference</span><span class="loc">Location goes here</span></div>

  <div class="abs tickets" style="left:600px;top:492px">
    <h2>Info and Tickets</h2>
    <div class="phone">+49 00 12 34 56 789</div>
    <div class="mail">tickets@ktrfestival.de</div>
  </div>

  <!-- right panel -->
  <div class="photo" role="img" aria-label="Foto eines Chors mit Dirigentin unter einem Bühnendach" style="left:861px;top:0;width:291px;height:186px"></div>
  <div class="abs artist right" style="left:874px;top:197px;width:265px">
    <h3>Artist or Band Name</h3>
    <h4>Title of the theme - <span>Music start h 10.00</span></h4>
    <p>Lorem ipsum dolor sit amet, consectetur adipiscing elit, sed do eiusmod tempor incididunt ut labore et dolore magna aliqua. Ut enim ad minim veniam, quis nostrud exercitation ullamco laboris nisi ut aliquip ex ea commodo consequat.</p>
  </div>
  <div class="photo" role="img" aria-label="Foto eines Blasorchesters mit Tuba und Notenständern" style="left:861px;top:301px;width:291px;height:156px"></div>
  <div class="abs artist right" style="left:874px;top:468px;width:265px">
    <h3>Artist or Band Name</h3>
    <h4>Title of the theme - <span>Music start h 10.00</span></h4>
    <p>Lorem ipsum dolor sit amet, consectetur adipiscing elit, sed do eiusmod tempor incididunt ut labore et dolore magna aliqua. Ut enim ad minim veniam, quis nostrud exercitation ullamco laboris nisi ut aliquip ex ea commodo consequat.</p>
  </div>

  <div class="pattern" role="img" aria-label="Geometrische Musterleiste am unteren Rand" style="left:0;top:566px;width:1152px;height:39px"></div>
</section>

</body>
</html>
```